Amber Moth Glen- Luxury Tree-house Wellness Resort Website

Amber Moth Glen is a luxury nature wellness resort. Please look at our current website for content information and aesthetic. Brand
ing, imaging and color pallet all stay the same. We need the website simplified and easier to understand and better flow visually. More use of videos. I can send additional photos or videos. I love whimsical and magical. We don’t need to add extra content.
We have a vintage storybook theme with rich woods, alligator leather, nautical compasses, ship wheel, we have skeleton keys to miniature doors. Think Tobias under the hill. The concept is for the guest to stay and enjoy their time. Not travel to see other things. No fishing, no excursions. All on site, animals, gardens, games, meditation tools, relaxing and recharging. Again, please keep the same text and pictures that’s on the website now. I like adding as many slow videos as possible

Target Market(s)

Luxury Travelers. Wealthy Tourists.

Industry/Entity Type

Luxury Nature and Wellness Resort

Coding

Coded - Design and coding required

Number of Pages Required

4 page

Font styles to use
Serif
Script

Requirements
Must have
• All the photos and descriptions that are currently on the website. videos in the background. motion, textures
Nice to have
• Please ADD More pictures of the people/experience. I would like to have a textured background and maybe a palm leaf that is stationary in the lower right corner of the website that stays still while you scroll.

```html
<!DOCTYPE html>
<html lang="en">
<head>
<meta charset="utf-8">
<title>Amber Moth Glen – Luxury Campground Resort</title>
<link href="https://fonts.googleapis.com/css2?family=Cinzel:wght@500;600;700&family=Lato:wght@400;700;900&family=Parisienne&display=swap" rel="stylesheet">
<style>
:root{
  --forest:#2a3a0c;
  --forest-deep:#223008;
  --gold:#e8d27c;
  --gold-deep:#c9a640;
  --ink:#1f1f1f;
  --muted:#555;
  --mist:#efece4;
  --parchment:#fbf8f1;
  --white:#fff;
}
*{box-sizing:border-box;margin:0;padding:0}
html,body{width:1200px;height:4902px;overflow:hidden}
body{font-family:'Lato',sans-serif;color:var(--ink);position:relative;
  background:
    radial-gradient(ellipse 600px 400px at 15% 10%,rgba(201,166,64,.07),transparent 70%),
    radial-gradient(ellipse 700px 500px at 85% 45%,rgba(120,90,40,.06),transparent 70%),
    radial-gradient(ellipse 600px 500px at 20% 80%,rgba(201,166,64,.06),transparent 70%),
    var(--parchment);}
.abs{position:absolute}
section,header,footer{position:relative;width:1200px;overflow:hidden}
.eyebrow{font-family:'Parisienne',cursive;font-size:21px;color:var(--gold-deep);text-align:center;line-height:1}
.title{font-family:'Cinzel',serif;font-weight:600;font-size:30px;text-align:center;letter-spacing:.5px;color:var(--ink)}
.rule{position:absolute;left:540px;width:120px;height:14px;display:flex;align-items:center;gap:8px}
.rule:before,.rule:after{content:"";flex:1;height:2px;background:var(--gold-deep)}
.rule i{width:10px;height:10px;border:2px solid var(--gold-deep);transform:rotate(45deg);flex:none}
.btn{position:absolute;display:flex;align-items:center;justify-content:center;gap:8px;border-radius:30px;font-weight:900;font-size:14px;text-transform:uppercase}
.btn-dark{background:var(--forest);color:var(--white)}
.btn-light{background:var(--white);color:var(--forest)}
.btn-outline{border:2px solid var(--forest);color:var(--forest);background:transparent}
.btn-ghost{border:2px solid var(--white);color:var(--white)}
.photo{position:absolute;overflow:hidden}
.slow-video{background-size:140% 140%!important;animation:drift 24s ease-in-out infinite alternate}
@keyframes drift{from{background-position:0% 0%}to{background-position:100% 100%}}
.video-tag{position:absolute;left:12px;bottom:12px;display:flex;align-items:center;gap:6px;background:rgba(0,0,0,.45);color:var(--white);font-size:11px;letter-spacing:1px;padding:5px 10px;border-radius:14px;text-transform:uppercase}
.video-tag:before{content:"";width:0;height:0;border-left:7px solid var(--gold);border-top:4px solid transparent;border-bottom:4px solid transparent}

/* header */
.site-header{height:106px;background:var(--white)}
.brand{left:140px;top:14px;width:110px;text-align:center}
.brand-dot{width:40px;height:40px;border-radius:50%;border:2px solid var(--ink);margin:0 auto 8px}
.brand-name{font-size:12px;letter-spacing:1.5px;text-transform:uppercase;color:var(--ink);line-height:15px}
.contact-chip{display:flex;align-items:center;gap:10px;top:10px}
.chip-icon{width:44px;height:44px;border-radius:50%;border:2px solid var(--forest);display:flex;align-items:center;justify-content:center}
.chip-label{font-size:10px;color:var(--muted)}
.chip-value{font-size:14px;color:var(--ink)}
.main-nav{top:77px;left:309px;display:flex;gap:22px;font-size:13.5px}
.main-nav .active{position:relative}
.main-nav .active:after{content:"";position:absolute;left:0;right:0;bottom:-9px;height:2px;background:var(--gold-deep)}

/* hero */
.hero{height:541px}
.hero-bg{inset:0;background:linear-gradient(100deg,#2c1e12 0%,#5a3d22 45%,#7a5433 70%,#3e2a18 100%)}
.hero-shade{inset:0;background:linear-gradient(90deg,rgba(0,0,0,.55),rgba(0,0,0,.05) 70%)}
.hero-kicker{left:143px;top:86px;color:var(--gold);font-family:'Parisienne',cursive;font-size:24px}
.hero h1{left:143px;top:118px;font-family:'Cinzel',serif;font-weight:600;font-size:52px;line-height:72px;color:var(--white);letter-spacing:1px}
.hero-copy{left:143px;top:268px;width:540px;color:var(--white);font-size:16px;line-height:28px}
.play{border-radius:50%;background:var(--white);display:flex;align-items:center;justify-content:center;box-shadow:0 0 0 8px rgba(255,255,255,.25)}
.hero .video-tag{left:1040px;bottom:20px}

/* accommodations */
.stays{height:1059px}
.stay-card{position:absolute;left:143px;width:912px;height:372px;background:var(--white);box-shadow:0 4px 22px rgba(0,0,0,.12);border:1px solid rgba(201,166,64,.35)}
.stay-body{position:absolute;top:30px;width:420px}
.badge{display:inline-block;background:var(--gold);font-size:10px;font-weight:700;padding:3px 12px;border-radius:10px}
.stay-body h3{font-weight:700;font-size:21px;margin:14px 0 22px}
.perks{display:grid;grid-template-columns:200px 200px;row-gap:7px;font-size:12.5px;color:#444}
.perks li{list-style:none;display:flex;align-items:center;gap:8px;white-space:nowrap}
.perks li:before{content:"";width:9px;height:9px;border-radius:50%;border:1.5px solid var(--gold-deep);flex:none}

/* packages */
.packages{height:586px;background:
  radial-gradient(ellipse 500px 300px at 20% 30%,rgba(255,255,255,.5),transparent 70%),
  radial-gradient(ellipse 500px 300px at 80% 80%,rgba(201,166,64,.08),transparent 70%),var(--mist)}
.tab{position:absolute;background:var(--white);display:flex;align-items:center;justify-content:center}
.tab span{font-size:16px;letter-spacing:1px;white-space:nowrap}
.arrow{position:absolute;width:36px;height:36px;border-radius:50%;background:var(--white);border:1px solid #bbb;display:flex;align-items:center;justify-content:center}
.feature{position:absolute;left:630px;top:227px;width:232px;height:292px;background:var(--gold);padding:26px 22px}
.feature .kicker{font-family:'Parisienne',cursive;font-size:16px}
.feature h4{font-size:18px;font-weight:900;margin:4px 0 16px}
.feature li{list-style:none;font-size:12.5px;display:flex;gap:8px;align-items:center;margin-bottom:7px}
.feature li:before{content:"";width:9px;height:9px;border-radius:50%;border:2px solid var(--forest);flex:none}
.feature .more{font-size:13px;font-weight:900;color:var(--forest);margin-top:18px;display:block}

/* availability */
.availability{height:321px;background:
  radial-gradient(ellipse 500px 260px at 10% 20%,rgba(255,255,255,.06),transparent 70%),
  radial-gradient(ellipse 500px 260px at 90% 90%,rgba(0,0,0,.25),transparent 70%),var(--forest)}
.availability .kicker{top:52px;width:100%;text-align:center;color:var(--gold);font-family:'Parisienne',cursive;font-size:22px}
.availability h2{top:82px;width:100%;text-align:center;font-family:'Cinzel',serif;font-weight:600;font-size:46px;color:var(--white);letter-spacing:1.5px}
.availability p{top:155px;width:100%;text-align:center;color:var(--white);font-size:16px}

/* video */
.film{height:666px}
.film-frame{left:210px;top:187px;width:780px;height:396px;border-radius:6px;background:linear-gradient(180deg,#2c3a5a 0%,#4a5578 40%,#3a2a1c 68%,#2a2520 100%);box-shadow:0 20px 24px -14px rgba(0,0,0,.35)}

/* reunions */
.retreats{height:367px;background:
  radial-gradient(ellipse 500px 250px at 20% 20%,rgba(255,255,255,.25),transparent 70%),
  radial-gradient(ellipse 500px 250px at 80% 90%,rgba(160,120,40,.15),transparent 70%),var(--gold)}
.retreat{position:absolute;top:168px;width:170px;text-align:center;font-size:14px}
.retreat .ring{width:96px;height:96px;border-radius:50%;background:var(--forest);border:3px solid #b9a24f;margin:0 auto 16px;display:flex;align-items:center;justify-content:center}

/* gallery */
.gallery{height:957px}

/* footer */
.site-footer{height:299px;background:var(--forest-deep);color:var(--white)}
.foot-nav{top:42px;width:100%;display:flex;justify-content:center;gap:30px;font-size:14px}
.foot-line{left:143px;width:912px;height:1px;background:rgba(255,255,255,.3)}
.foot-item{top:122px;display:flex;gap:18px;align-items:flex-start}
.foot-icon{width:48px;height:48px;border-radius:50%;background:var(--gold);display:flex;align-items:center;justify-content:center;flex:none}
.foot-label{color:var(--gold);font-size:13px;letter-spacing:.5px;text-transform:uppercase}
.foot-val{font-size:13px;margin-top:6px;line-height:20px}
.foot-note{font-size:10px;margin-top:4px}
.divider-v{top:120px;width:1px;height:80px;background:rgba(255,255,255,.3)}
.copyright{bottom:18px;width:100%;text-align:center;font-size:11px}

/* stationary palm leaf */
.palm-leaf{position:fixed;right:0;bottom:0;width:170px;height:240px;z-index:20;pointer-events:none;
  background:linear-gradient(200deg,#5f7a2a,#2f4a12 70%);opacity:.85;
  border-radius:100% 0 0 0 / 100% 0 0 0}
</style>
</head>
<body>

<header class="site-header">
  <div class="abs brand">
    <div class="brand-dot"></div>
    <div class="brand-name">Amber Moth Glen</div>
  </div>
  <div class="abs contact-chip" style="left:345px">
    <div class="chip-icon"><svg width="20" height="16" viewBox="0 0 20 16"><rect x="1" y="1" width="18" height="14" fill="none" stroke="#2a3a0c" stroke-width="2"/><path d="M1 1l9 8 9-8" fill="none" stroke="#2a3a0c" stroke-width="2"/></svg></div>
    <div><div class="chip-label">EMAIL US:</div><div class="chip-value">headquarters@ambermothglen.com</div></div>
  </div>
  <div class="abs contact-chip" style="left:655px">
    <div class="chip-icon"><svg width="20" height="20" viewBox="0 0 24 24"><path d="M6 2l4 5-2 3c1 3 3 5 6 6l3-2 5 4-2 4C10 22 2 14 2 4z" fill="#2a3a0c"/></svg></div>
    <div><div class="chip-label">CALL US:</div><div class="chip-value">555-208-2030</div></div>
  </div>
  <div class="btn btn-dark" style="left:830px;top:12px;width:225px;height:44px;border-radius:22px;font-size:13px">Plan Your Adventure</div>
  <nav class="abs main-nav">
    <span class="active">Home</span><span>Accommodations</span><span>Reunions &amp; Retreats</span><span>Packages</span><span>Travel Guide</span><span>Gallery</span><span>Contact</span><span>Solenne Resorts</span>
  </nav>
</header>

<section class="hero">
  <div class="abs hero-bg slow-video" role="img" aria-label="Slow background video of a wooden treehouse cabin with shuttered windows among trees"></div>
  <div class="abs hero-shade"></div>
  <div class="abs hero-kicker">Luxury Campground Resort</div>
  <h1 class="abs">WELCOME TO<br>AMBER MOTH GLEN</h1>
  <p class="abs hero-copy">Elevated Treehouses. Curated Surprises. Unforgettable Gatherings. Retreats. Nature Immersion. Wildlife Viewing. Campfires. Designed for Memories. Exclusive Privacy. Disconnect to Connect.</p>
  <div class="btn btn-light" style="left:143px;top:393px;width:185px;height:46px">Inquire Now <span>›</span></div>
  <div class="abs play" style="left:884px;top:231px;width:60px;height:60px"><svg width="20" height="22" viewBox="0 0 20 22"><path d="M2 1l17 10L2 21z" fill="#1f1f1f"/></svg></div>
  <span class="video-tag">Slow Film</span>
</section>

<section class="stays">
  <div class="abs eyebrow" style="top:70px;width:100%">Custom Curated Adventures</div>
  <h2 class="abs title" style="top:103px;width:100%">ACCOMMODATIONS</h2>
  <div class="rule" style="top:151px"><i></i></div>

  <article class="stay-card" style="top:208px">
    <div class="photo slow-video" style="left:0;top:0;width:457px;height:372px;background:linear-gradient(160deg,#3b2516,#6b4427 45%,#2a1a10)" role="img" aria-label="Slow video of the main house interior with wood walls, staircase and fireplace"><span class="video-tag">Slow Film</span></div>
    <div class="stay-body" style="left:482px">
      <span class="badge">Main House</span>
      <h3>BELLWETHER</h3>
      <ul class="perks">
        <li>Hosts 17 Guests</li><li>Games &amp; Music Nights</li>
        <li>Hot Tub</li><li>5 Bedrooms &amp; 5 Bunk Beds</li>
        <li>Campfire, BBQ &amp; Smores</li><li>Sleeps 9 Adults &amp; 8</li>
        <li>Chef's Kitchen</li><li>Children</li>
        <li>Hidden Treasure Rooms</li><li>3.5 Bathrooms</li>
        <li>Mini Golf, Swings</li><li>Curated Surprises</li>
        <li>Sleeping Porch</li>
      </ul>
    </div>
    <div class="btn btn-dark" style="left:482px;top:296px;width:216px;height:44px;font-size:13px">Discover Bellwether <span>›</span></div>
  </article>

  <article class="stay-card" style="top:608px">
    <div class="stay-body" style="left:20px">
      <span class="badge">Luxury Tents</span>
      <h3>TREE-HOUSE TENTS</h3>
      <ul class="perks" style="grid-template-columns:225px 180px">
        <li>Custom Curated Tree-house Tents</li><li>Outdoor Dining</li>
        <li>Marsh and River Front</li><li>Wildlife Viewing Porches</li>
        <li>Serene Nature Setting</li><li>Bed Swings</li>
        <li>Ultimate Privacy and Exclusivity</li><li>Outdoor Soaking Tubs</li>
        <li>Fully Climate Controlled</li><li>Hidden Treasure</li>
        <li>Bathrooms with Tile Showers</li><li>Games &amp; Music Nights</li>
        <li>Campsite with BBQ and Grilling</li>
      </ul>
    </div>
    <div class="btn btn-dark" style="left:20px;top:297px;width:252px;height:44px;font-size:13px">Discover Our Treehouse Tents <span>›</span></div>
    <div class="photo slow-video" style="left:457px;top:0;width:455px;height:372px;background:linear-gradient(180deg,#2b1d12,#6e3e16 55%,#b7772d 80%,#4a3220)" role="img" aria-label="Slow video of a lit treehouse tent at night with campfire under oak trees"><span class="video-tag">Slow Film</span></div>
  </article>
</section>

<section class="packages">
  <div class="abs eyebrow" style="top:54px;width:100%">Packages</div>
  <h2 class="abs title" style="top:80px;width:100%;line-height:48px">CUSTOM CURATED ADVENTURES &amp; PACKAGES<br>FOR EACH GUEST</h2>
  <div class="arrow" style="left:80px;top:356px"><svg width="10" height="14"><path d="M8 1L2 7l6 6" fill="none" stroke="#333" stroke-width="2"/></svg></div>
  <div class="arrow" style="left:1083px;top:356px"><svg width="10" height="14"><path d="M2 1l6 6-6 6" fill="none" stroke="#333" stroke-width="2"/></svg></div>
  <div class="tab" style="left:143px;top:254px;width:57px;height:240px"><span style="transform:rotate(-90deg)">CULINARY</span></div>
  <div class="photo slow-video" style="left:200px;top:254px;width:138px;height:240px;background:linear-gradient(135deg,#c7482a,#e8b57a 55%,#d9d2c4)" role="img" aria-label="Seafood platter with lobster and crab"></div>
  <div class="photo slow-video" style="left:338px;top:241px;width:292px;height:266px;background:linear-gradient(135deg,#6f7a53,#9aa17a 50%,#4d4a36)" role="img" aria-label="Slow video of a cardinal bird perched on a branch"><span class="video-tag">Slow Film</span></div>
  <div class="feature">
    <div class="kicker">Discover The Magic</div>
    <h4>ADVENTURE</h4>
    <ul>
      <li>Outdoor Dining</li><li>Wildlife Viewing Porches</li><li>Bed Swings</li><li>Outdoor Soaking Tubs</li><li>Hidden Treasure</li><li>Games &amp; Music Nights</li>
    </ul>
    <span class="more">LEARN MORE ›</span>
  </div>
  <div class="photo slow-video" style="left:862px;top:254px;width:138px;height:240px;background:linear-gradient(135deg,#5e6b5a,#9b8a6a 60%,#b38a4a)" role="img" aria-label="Relaxation session with singing bowl"></div>
  <div class="tab" style="left:1000px;top:254px;width:55px;height:240px"><span style="transform:rotate(90deg)">RELAXATION</span></div>
</section>

<section class="availability">
  <div class="abs kicker">Immerse Yourself In Coastal Culture &amp; Wildlife</div>
  <h2 class="abs">LIMITED SEASONAL AVAILABILITY</h2>
  <p class="abs">Curated Guest Experiences Privacy By Design</p>
  <div class="btn btn-ghost" style="left:512px;top:218px;width:176px;height:43px">Inquire Now <span>›</span></div>
</section>

<section class="film">
  <div class="abs eyebrow" style="top:68px;width:100%">Watch Our Video</div>
  <h2 class="abs title" style="top:98px;width:100%">WHERE TIME STANDS STILL &amp; STORIES BEGIN</h2>
  <div class="rule" style="top:147px"><i></i></div>
  <div class="photo film-frame slow-video" role="img" aria-label="Slow video of lit treehouse cabins under oak trees at dusk"></div>
  <div class="abs play" style="left:570px;top:355px;width:60px;height:60px"><svg width="20" height="22" viewBox="0 0 20 22"><path d="M2 1l17 10L2 21z" fill="#1f1f1f"/></svg></div>
</section>

<section class="retreats">
  <div class="abs eyebrow" style="top:54px;width:100%;color:var(--forest)">A Place to Reconnect</div>
  <h2 class="abs title" style="top:84px;width:100%">REUNIONS &amp; RETREATS</h2>
  <div class="rule" style="top:133px"><i style="border-color:var(--forest)"></i></div>
  <svg class="abs" style="left:92px;top:220px" width="12" height="18"><path d="M10 2L3 9l7 7" fill="none" stroke="#222" stroke-width="2"/></svg>
  <svg class="abs" style="left:1094px;top:220px" width="12" height="18"><path d="M2 2l7 7-7 7" fill="none" stroke="#222" stroke-width="2"/></svg>
  <div class="retreat" style="left:115px"><div class="ring"><svg width="44" height="44" viewBox="0 0 44 44" fill="none" stroke="#e8d27c" stroke-width="2"><circle cx="14" cy="12" r="5"/><circle cx="30" cy="12" r="5"/><path d="M6 38V24h16v14M22 38V24h16v14"/></svg></div>Family Reunions</div>
  <div class="retreat" style="left:325px"><div class="ring"><svg width="44" height="44" viewBox="0 0 44 44" fill="none" stroke="#e8d27c" stroke-width="2"><rect x="8" y="20" width="28" height="16"/><rect x="12" y="12" width="20" height="8"/><path d="M16 6v6M22 6v6M28 6v6"/></svg></div>Birthday Parties</div>
  <div class="retreat" style="left:529px"><div class="ring"><svg width="44" height="44" viewBox="0 0 44 44" fill="none" stroke="#e8d27c" stroke-width="2"><path d="M6 10l10-3 12 4 10-3v26l-10 3-12-4-10 3z"/><path d="M22 18l6 6M28 18l-6 6"/></svg></div>Treasure Hunts</div>
  <div class="retreat" style="left:728px"><div class="ring"><svg width="44" height="44" viewBox="0 0 44 44" fill="none" stroke="#e8d27c" stroke-width="2"><circle cx="14" cy="30" r="6"/><circle cx="30" cy="30" r="6"/><path d="M20 30h4M22 24l6-12 6 2"/></svg></div>Bird Watching</div>
  <div class="retreat" style="left:921px"><div class="ring"><svg width="44" height="44" viewBox="0 0 44 44" fill="none" stroke="#e8d27c" stroke-width="2"><path d="M6 36V20l16-12 16 12v16z"/><rect x="17" y="24" width="10" height="12"/></svg></div>Farm Animals</div>
</section>

<section class="gallery">
  <div class="abs eyebrow" style="top:72px;width:100%">Our Gallery</div>
  <h2 class="abs title" style="top:104px;width:100%">SCENES TO REMEMBER</h2>
  <div class="photo slow-video" style="left:143px;top:200px;width:296px;height:217px;background:linear-gradient(160deg,#6a5a40,#8f7a55 50%,#4c3b28)" role="img" aria-label="Slow video of a wooden porch swing overlooking trees"><span class="video-tag">Slow Film</span></div>
  <div class="photo" style="left:143px;top:428px;width:296px;height:358px;background:linear-gradient(160deg,#6a4e36,#a89d92 55%,#5b4634)" role="img" aria-label="Rabbit sitting indoors"></div>
  <div class="photo" style="left:452px;top:200px;width:296px;height:359px;background:linear-gradient(170deg,#3f3a2e,#6d6450 50%,#8b8472)" role="img" aria-label="Birdhouse on a tree trunk near a treehouse"></div>
  <div class="photo" style="left:452px;top:570px;width:296px;height:216px;background:linear-gradient(160deg,#56603f,#7f7660 55%,#4b4538)" role="img" aria-label="Squirrel perched on a tree stump"></div>
  <div class="photo slow-video" style="left:761px;top:200px;width:294px;height:217px;background:linear-gradient(170deg,#3d5f88,#7b6a52 55%,#3f3a2a)" role="img" aria-label="Slow video of a treehouse tent among live oaks"><span class="video-tag">Slow Film</span></div>
  <div class="photo" style="left:761px;top:428px;width:294px;height:358px;background:linear-gradient(170deg,#6b7f95,#566048 55%,#3a3a2c)" role="img" aria-label="Miniature house on a mossy oak tree"></div>
  <div class="btn btn-dark" style="left:433px;top:834px;width:151px;height:44px">View More <span>›</span></div>
  <div class="btn btn-outline" style="left:592px;top:834px;width:175px;height:44px">Inquire Now <span>›</span></div>
</section>

<footer class="site-footer">
  <nav class="abs foot-nav"><span>Home</span><span>Accommodations</span><span>Reunions &amp; Retreats</span><span>Packages</span><span>Travel Guide</span><span>Gallery</span><span>Contact</span><span>Solenne Resorts</span></nav>
  <div class="abs foot-line" style="top:90px"></div>
  <div class="abs foot-item" style="left:143px">
    <div class="foot-icon"><svg width="22" height="16" viewBox="0 0 20 16"><rect x="1" y="1" width="18" height="14" fill="none" stroke="#fff" stroke-width="1.6"/><path d="M1 1l9 8 9-8" fill="none" stroke="#fff" stroke-width="1.6"/></svg></div>
    <div><div class="foot-label">Email Address</div><div class="foot-val">headquarters@ambermothglen.com</div><div class="foot-note">Email Us</div></div>
  </div>
  <div class="abs divider-v" style="left:457px"></div>
  <div class="abs foot-item" style="left:493px">
    <div class="foot-icon"><svg width="20" height="20" viewBox="0 0 24 24"><path d="M6 2l4 5-2 3c1 3 3 5 6 6l3-2 5 4-2 4C10 22 2 14 2 4z" fill="none" stroke="#fff" stroke-width="1.6"/></svg></div>
    <div><div class="foot-label">Phone Number</div><div class="foot-val">555-208-2030</div><div class="foot-note">Call Us On</div></div>
  </div>
  <div class="abs divider-v" style="left:732px"></div>
  <div class="abs foot-item" style="left:793px">
    <div class="foot-icon"><svg width="20" height="22" viewBox="0 0 20 22"><path d="M10 21s7-7 7-12a7 7 0 0 0-14 0c0 5 7 12 7 12z" fill="none" stroke="#fff" stroke-width="1.6"/><circle cx="10" cy="9" r="2.5" fill="none" stroke="#fff" stroke-width="1.6"/></svg></div>
    <div><div class="foot-label">Location</div><div class="foot-val">48 Fernhollow Lane<br>Marshvale, GA 30418</div><div class="foot-note">Our Office</div></div>
  </div>
  <div class="abs foot-line" style="top:228px"></div>
  <div class="abs copyright">2026 Copyright © Amber Moth Glen - Privacy Policy - Terms of Use - ADA</div>
</footer>

<div class="palm-leaf" role="img" aria-label="Stationary palm leaf resting in the lower right corner"></div>

</body>
</html>
```